MerrowtonPlatformKit Explainer

We are looking for an attractive/moderan info graphics that will explain our software and how it helps driving schools to fully integrated their business with clients and staff.
Attached word doc outlines the description of the main modules and most important services that our software performs.
The info graphic should be easy to read and understand as the main audience of school owners is not technically savvy and are generally averse to technology and computers.

Target Market(s)

Driving school owners and managers

Industry/Entity Type

Driving School

Font styles to use
Sans Serif

Colors

Designer to choose colors to be used in the design.

Requirements
Must have
• Clear graphics that complement logo colors. Easy to read understand.
Should not have
• complicated and confusing text.

```html
<!DOCTYPE html>
<html lang="en">
<head>
<meta charset="utf-8">
<title>MerrowtonPlatformKit Explainer</title>
<link href="https://fonts.googleapis.com/css2?family=Roboto:wght@400;500;700&display=swap" rel="stylesheet">
<style>
  :root{
    --navy:#1d4f91;
    --navy-dark:#163d70;
    --green:#4caf3f;
    --green-text:#3fa336;
    --shadow:#1e5a3a;
    --white:#ffffff;
    --ink:#222;
    --skin:#e8c4a8;
    --frame:#2a5d9f;
  }
  *{box-sizing:border-box;margin:0;padding:0}
  html,body{width:1200px;height:4675px;overflow:hidden;background:var(--white)}
  body{position:relative;font-family:"Roboto",Arial,sans-serif;color:var(--ink)}
  .abs{position:absolute}
  .hero-scene{left:47px;top:47px;width:405px;height:389px;border:10px solid var(--frame);border-radius:18px;
    background:linear-gradient(180deg,#cfd6de 0%,#9aa6b3 55%,#3a3f47 100%)}
  .hero-device{left:608px;top:78px;width:530px;height:343px;border-radius:18px;
    background:linear-gradient(180deg,#f4f6f8 0%,#dfe4ea 100%);border:8px solid #2c2f36;
    display:flex;align-items:center;justify-content:center}
  .brand-name{font-weight:700;color:var(--navy);font-size:44px;display:flex;align-items:center;gap:14px}
  .brand-dot{width:34px;height:34px;border-radius:50%;background:var(--green)}
  .intro{left:0;width:1200px;text-align:center;color:var(--navy);font-weight:700}
  .intro-title{top:462px;font-size:46px}
  .intro-sub{top:514px;font-size:46px}
  .intro-rule{left:180px;top:582px;width:840px;height:3px;background:var(--green)}
  .intro-modules{top:596px;font-size:40px;color:var(--green-text)}
  .module-card{width:465px;height:312px;border:6px solid var(--navy);border-radius:26px;overflow:hidden;background:var(--white)}
  .module-art{width:100%;height:100%;display:flex;align-items:center;justify-content:center}
  .art-person{background:linear-gradient(180deg,#eef3f8 0%,#c9d6e4 100%)}
  .art-laptop{background:linear-gradient(180deg,#f4f4f4 0%,#2d2f34 100%)}
  .module-label{width:465px;text-align:center;font-weight:700;color:var(--ink);font-size:30px;line-height:38px}
  .section-title{width:340px;text-align:center;font-weight:700;color:var(--navy);font-size:46px;line-height:54px}
  .section-rule{height:2px;background:#c9ced6;width:300px}
  .section-art{width:374px;height:259px;border:5px solid var(--navy);border-radius:26px;overflow:visible}
  .section-art .module-art{border-radius:20px}
  .section-art::after{content:"";position:absolute;right:-44px;top:40px;width:0;height:0;
    border-top:20px solid transparent;border-bottom:20px solid transparent;border-left:44px solid var(--navy)}
  .detail-box{left:483px;width:677px;border-radius:28px;background:var(--green);
    box-shadow:14px 14px 0 var(--shadow);color:var(--white);
    display:flex;flex-direction:column;justify-content:center;padding:20px 34px}
  .detail-box ul{list-style:none}
  .detail-box li{font-size:33px;line-height:40px;text-indent:0}
  .detail-box li::before{content:"";display:inline-block;width:14px;height:14px;border-radius:50%;
    background:var(--navy);margin:0 26px 6px 20px;vertical-align:middle}
  .auto-box{left:47px;top:3896px;width:1106px;height:281px;border:6px solid var(--navy);border-radius:24px;background:var(--white)}
  .auto-title{left:34px;top:22px;color:var(--navy);font-weight:500;font-size:32px}
  .auto-icon{left:30px;top:90px}
  .auto-list{left:110px;top:82px;list-style:none}
  .auto-list li{color:var(--green-text);font-weight:700;font-size:32px;line-height:42px}
  .auto-list li::before{content:"";display:inline-block;width:13px;height:13px;border-radius:50%;
    background:var(--navy);margin:0 30px 6px -30px;vertical-align:middle}
  .footer-brand{left:0;top:4380px;width:1200px;display:flex;justify-content:center}
  .footer-brand .brand-name{font-size:72px;gap:22px}
  .footer-brand .brand-dot{width:60px;height:60px}
</style>
</head>
<body>

<div class="abs hero-scene" role="img" aria-label="Illustration of a driver's hands on a steering wheel viewed from inside a car"></div>
<div class="abs hero-device" role="img" aria-label="Illustration of a laptop and smartphone showing the software">
  <div class="brand-name"><span class="brand-dot"></span>MerrowtonPlatformKit</div>
</div>

<div class="abs intro intro-title">Service description</div>
<div class="abs intro intro-sub">Web based software designed for driving schools.</div>
<div class="abs intro-rule"></div>
<div class="abs intro intro-modules">Software consists of 4 major modules:</div>

<div class="abs module-card" style="left:87px;top:664px"><div class="module-art art-person" role="img" aria-label="Illustration of an administrator in a suit"></div></div>
<div class="abs module-card" style="left:636px;top:664px"><div class="module-art art-laptop" role="img" aria-label="Illustration of a laptop showing the enrollment website"></div></div>
<div class="abs module-label" style="left:87px;top:988px">Administrative</div>
<div class="abs module-label" style="left:636px;top:988px">Website enrollment</div>

<div class="abs module-card" style="left:87px;top:1050px"><div class="module-art art-person" role="img" aria-label="Illustration of a student and parent holding a tablet"></div></div>
<div class="abs module-card" style="left:636px;top:1050px"><div class="module-art art-person" role="img" aria-label="Illustration of an instructor holding a tablet"></div></div>
<div class="abs module-label" style="left:87px;top:1385px">Student and Parent Center</div>
<div class="abs module-label" style="left:636px;top:1385px">Instructor and Staff<br>Smart phone access</div>

<!-- Administrative -->
<div class="abs section-title" style="left:56px;top:1646px">Administrative</div>
<div class="abs section-art" style="left:56px;top:1720px"><div class="module-art art-person" role="img" aria-label="Illustration of an administrator in a suit"></div></div>
<div class="abs detail-box" style="top:1527px;height:624px">
  <ul>
    <li>All main administrative functions are accomplished.</li>
    <li>Admins can create student accounts, enroll them and manage student payments</li>
    <li>Create lessons and classroom</li>
    <li>Run business reports</li>
    <li>Create State Forms for compliance</li>
    <li>Schedule Student lessons and take classroom attendance</li>
    <li>Track vehicles via GPS and manage vehicle maintenance</li>
    <li>Send and receive text messages from students and parents</li>
  </ul>
</div>

<!-- Website enrollment -->
<div class="abs section-rule" style="left:80px;top:2197px"></div>
<div class="abs section-title" style="left:56px;top:2216px">Website<br>enrollment</div>
<div class="abs section-art" style="left:56px;top:2360px"><div class="module-art art-laptop" role="img" aria-label="Illustration of a laptop showing the enrollment website"></div></div>
<div class="abs detail-box" style="top:2188px;height:424px">
  <ul>
    <li>This module allows school to receive enrollments directly from their website and all information is saved directly into the schools database</li>
    <li>Website enrollments can also process credit card payments</li>
    <li>Student accounts are automatically created without any staff effort</li>
  </ul>
</div>

<!-- Student and Parent Center -->
<div class="abs section-rule" style="left:80px;top:2749px"></div>
<div class="abs section-title" style="left:56px;top:2768px">Student and<br>Parent Center</div>
<div class="abs section-art" style="left:56px;top:2899px"><div class="module-art art-person" role="img" aria-label="Illustration of a student and parent holding a tablet"></div></div>
<div class="abs detail-box" style="top:2696px;height:624px">
  <ul>
    <li>Each student has the ability to access their own account and view status</li>
    <li>They can pay for any open balances</li>
    <li>They can view status of their program</li>
    <li>They can purchase additional services</li>
    <li>They can schedule in-car lessons</li>
    <li>They can schedule classroom makeup session</li>
    <li>They can contact school</li>
    <li>They can access their account from any device anytime</li>
  </ul>
</div>

<!-- Instructor -->
<div class="abs section-title" style="left:56px;top:3312px">Instructor and<br>Staff Smart<br>phone access</div>
<div class="abs section-art" style="left:56px;top:3497px"><div class="module-art art-person" role="img" aria-label="Illustration of an instructor holding a tablet"></div></div>
<div class="abs detail-box" style="top:3391px;height:443px">
  <ul>
    <li>Staff can and view their schedule in real time</li>
    <li>They can view students current program status</li>
    <li>They can complete lessons and take classroom attendance</li>
    <li>They can take electronic in-car evaluation</li>
    <li>Evaluation is sent in real-time to parent upon completion</li>
  </ul>
</div>

<!-- Automatic features -->
<div class="abs auto-box">
  <div class="abs auto-title">AUTOMATIC FEATURES</div>
  <svg class="abs auto-icon" width="56" height="120" viewBox="0 0 56 120" aria-hidden="true">
    <rect x="3" y="3" width="50" height="114" rx="8" fill="#fff" stroke="#1d4f91" stroke-width="5"/>
    <rect x="12" y="44" width="32" height="22" fill="#1d4f91"/>
    <path d="M12 44 L28 58 L44 44" fill="none" stroke="#fff" stroke-width="3"/>
    <circle cx="44" cy="76" r="9" fill="#e53935"/>
  </svg>
  <ul class="abs auto-list">
    <li>Email notifications for in-car lessons and classroom session</li>
    <li>Email notifications for new purchases and payments</li>
    <li>On-demand email notifications to individual parents/students</li>
    <li>Text message reminders for in car and class lessons.</li>
  </ul>
</div>

<div class="abs footer-brand">
  <div class="brand-name"><span class="brand-dot"></span>MerrowtonPlatformKit</div>
</div>

</body>
</html>
```